Business Cards for new orthopaedic surgery practice

My husband and I are starting our own orthopaedic surgery practice. We are looking for a business card that is uniform, but one will have my name/title and the other will have his. You can just create one design with my name on it for now. But when I choose your design as the winning design I will ask that you add another copy with his name/title.

We are looking for classy, simple, elite all in one. We like dark blues/a little gold/yellow. Something that goes with our logo. We want our logo incorporated. Here is all the info you need:
Business name: RV Spine & Vitality Center
Location: 38915 North Bramble Ave
Maple Hollow, FL 33419
Phone: 954-218-4630
Fax: 954-571-2846
Email: info@myrvspine.example

Names: Lucinda Ferrow, M.D.
Board Certified Hand and Upper Extremity Surgeon

Emeka Dlunga, M.D.
Board Certified Hip & Knee Replacement/General Orthopaedic Surgeon

Can decide what you want to put on the back. Maybe a slogan:
Grounded in Skill. Centered on You

I am just going to upload our logo. The only thing is if we select you as the winning design, the location, and phone numbers may change. We will need your help to update that once fully solidified.

Industry/Entity Type

Medical

Contact Information for Business Card

Colors
0054AA
0677BA
7BADD7
CADEEF
E8F1F8
0094D4
00A9DD
6FCCEA
C7EBF8
E9F6FB

Requirements
Must have
• class, appeal,
Should not have
• We want to air on the side of masculine if we are looking at masculine vs. feminine feel. But we still want it classy, sophisticated, and something we will love

```html
<!DOCTYPE html>
<html lang="en">
<head>
<meta charset="utf-8">
<title>RV Spine &amp; Vitality Center — Business Cards</title>
<link rel="stylesheet" href="https://fonts.googleapis.com/css2?family=Libre+Caslon+Text:wght@400;700&display=swap">
<style>
  :root {
    --navy: #14244f;
    --navy-deep: #0f1c40;
    --gold: #c89b4c;
    --white: #f7f5f0;
    --pattern: #34488a;
    --backdrop: #e6e6e8;
  }
  * { box-sizing: border-box; margin: 0; padding: 0; }
  html, body {
    width: 1200px; height: 801px; overflow: hidden;
    background: var(--backdrop);
    font-family: "Libre Caslon Text", "Times New Roman", serif;
  }
  .sheet {
    position: relative; width: 1200px; height: 801px;
    display: flex; align-items: center; justify-content: center; gap: 40px;
  }
  .card {
    position: relative; width: 540px; height: 309px;
    background: linear-gradient(135deg, var(--navy) 0%, var(--navy-deep) 100%);
    border: 2px solid var(--gold);
    box-shadow: 0 10px 24px rgba(20, 30, 60, 0.25);
    overflow: hidden; color: var(--white);
  }
  /* Front */
  .card-front .corner-tab {
    position: absolute; top: 0; right: 18px; width: 16px; height: 26px;
    background: var(--gold);
  }
  .identity {
    position: absolute; top: 34px; right: 28px; text-align: right;
  }
  .identity .person-name {
    font-size: 20px; font-weight: 700; color: var(--gold); letter-spacing: 0.2px;
  }
  .identity .person-title {
    font-size: 12px; margin-top: 4px; color: var(--white);
  }
  .identity .address {
    margin-top: 20px; font-size: 13.5px; line-height: 1.45;
  }
  .brand-mark {
    position: absolute; display: flex; align-items: center; gap: 10px;
    color: var(--white); font-weight: 400; text-transform: uppercase;
  }
  .brand-mark .brand-dot {
    flex: none; border-radius: 50%; border: 1.5px solid var(--gold);
  }
  .card-front .brand-mark {
    left: 26px; top: 118px; font-size: 13px; letter-spacing: 2.2px; line-height: 1.5;
  }
  .card-front .brand-mark .brand-dot { width: 42px; height: 42px; }
  .contacts {
    position: absolute; left: 26px; bottom: 22px; list-style: none;
    font-size: 13.5px; line-height: 1.55;
  }
  .contacts li { display: flex; align-items: center; gap: 8px; }
  .contacts svg { width: 13px; height: 13px; fill: var(--gold); flex: none; }
  /* Back */
  .pattern-field {
    position: absolute; inset: 0;
    background: linear-gradient(100deg, rgba(20,36,79,0) 0%, rgba(52,72,138,0.25) 55%, rgba(52,72,138,0.55) 100%);
  }
  .card-back .brand-mark {
    left: 50%; top: 50%; transform: translate(-50%, -62%);
    flex-direction: column; gap: 14px; text-align: center;
    font-size: 17px; letter-spacing: 3px; line-height: 1.5;
  }
  .card-back .brand-mark .brand-dot { width: 70px; height: 70px; }
  .tagline {
    position: absolute; left: 0; right: 0; bottom: 28px; text-align: center;
    color: var(--gold); font-size: 16px; font-weight: 700; letter-spacing: 0.3px;
  }
</style>
</head>
<body>
<main class="sheet">
  <section class="card card-front" aria-label="Business card front">
    <span class="corner-tab"></span>
    <div class="identity">
      <p class="person-name">Lucinda Ferrow, M.D.</p>
      <p class="person-title">Board Certified Hand and Upper Extremity Surgeon</p>
      <p class="address">38915 North Bramble Ave<br>Maple Hollow, FL 33419</p>
    </div>
    <div class="brand-mark">
      <span class="brand-dot"></span>
      <span>RV Spine &amp;<br>Vitality Center</span>
    </div>
    <ul class="contacts">
      <li><svg viewBox="0 0 24 24" aria-hidden="true"><path d="M6.6 10.8a15 15 0 0 0 6.6 6.6l2.2-2.2c.3-.3.7-.4 1-.2 1.1.4 2.3.6 3.6.6.6 0 1 .4 1 1V20c0 .6-.4 1-1 1A17 17 0 0 1 3 4c0-.6.4-1 1-1h3.5c.6 0 1 .4 1 1 0 1.3.2 2.5.6 3.6.1.3 0 .7-.2 1z"/></svg>954-218-4630</li>
      <li><svg viewBox="0 0 24 24" aria-hidden="true"><path d="M6 2h10l2 2v5H6zM4 10h16a2 2 0 0 1 2 2v6h-4v4H6v-4H2v-6a2 2 0 0 1 2-2zm4 7v3h8v-3z"/></svg>954-571-2846</li>
      <li><svg viewBox="0 0 24 24" aria-hidden="true"><path d="M2 5h20v14H2zm2 2v.4l8 5 8-5V7zm0 2.8V17h16V9.8l-8 5z"/></svg>info@myrvspine.example</li>
    </ul>
  </section>

  <section class="card card-back" aria-label="Business card back">
    <div class="pattern-field" role="img" aria-label="Repeating embossed brand pattern in deep and mid blue"></div>
    <div class="brand-mark">
      <span class="brand-dot"></span>
      <span>RV Spine &amp;<br>Vitality Center</span>
    </div>
    <p class="tagline">Grounded in Skill. Centered on You</p>
  </section>
</main>
</body>
</html>
```